Business card

I am a contemporary jeweller from Melbourne, Australia. I am after a great crisp and sophisticated business card. My ideas are very specific and I have a few files attached which are pretty much what I am after but i believe it needs refining and also the quality is too poor for printing, so it would need to be cleaned up a lot.

On one side I would like a logo with my initials (similar to the files I have attached - but a little more aesthetically pleasing) to somewhat match the font that I have attached. I would like a C and a G in lower case to be "hugging" each other - with the g inside the c. I want it to look like letters but also be attractive. I would also like it to look round and neat. The logo should look like a jeweller's hallmark stamp (as this logo will also be used as my Hallmark, and therefore needs to be crisp, sharp and simple so that it reads well on a small scale (2mm) and also on print media).

The business card layout should be on one side - my logo placed somewhere not very large and that is all.

on the other side of the card i would like my contact details without the logo anywhere.

I have attached what I would like the back of my card to look like, and also the font which I like which i found on www.typevarn.com called "The Skinny" and "The Skinny Bold". I love this font, but it loses quality when the size is reduced. I am unsure of what the font should be for my contact details so I am open to suggestions. I do feel that it should be different to The Skinny font and probably lower case.

I know that the following is not something that is in your control but it may give you an idea of what I like:
I will be having the business cards printed on quite thick and textured card and possibly embossed. It will be black font on white or off white paper.
Also, please find attached images of a business card I really like.

Thanks,
If you have any questions please contact me.

Industry/Entity Type

Business

Requirements
Nice to have
• DESNA PILOU (The Skinny Font or similar)
• Jeweller - designer
• fine contemporary jewellery
• +61 428 519 203
• info@desnapilou.com
• www.desnapilou.com

```html
<!DOCTYPE html>
<html lang="en">
<head>
<meta charset="utf-8">
<title>Desna Pilou — Business Card</title>
<link rel="stylesheet" href="https://fonts.googleapis.com/css2?family=Amatic+SC:wght@400;700&family=Montserrat:wght@400;500&display=swap">
<style>
  :root {
    --backdrop: #e9e7e4;
    --card: #fbfbfb;
    --card-edge: #e2e2e2;
    --ink: #111111;
    --shadow: rgba(0, 0, 0, 0.18);
  }
  * { margin: 0; padding: 0; box-sizing: border-box; }
  html, body {
    width: 1200px;
    height: 1000px;
    overflow: hidden;
    background: var(--backdrop);
  }
  .canvas {
    position: relative;
    width: 1200px;
    height: 1000px;
  }
  .card {
    position: absolute;
    width: 560px;
    height: 320px;
    background: linear-gradient(135deg, #ffffff 0%, var(--card) 60%, #f1f1f1 100%);
    border: 1px solid var(--card-edge);
    box-shadow: 0 14px 30px var(--shadow);
    color: var(--ink);
  }
  .card--front {
    left: 90px;
    top: 150px;
    display: flex;
    flex-direction: column;
    align-items: center;
    justify-content: center;
    gap: 14px;
  }
  .brand {
    display: flex;
    align-items: center;
    gap: 14px;
  }
  .brand__dot {
    width: 14px;
    height: 14px;
    border: 1.5px solid var(--ink);
    border-radius: 50%;
  }
  .brand__name {
    font-family: "Amatic SC", sans-serif;
    font-weight: 700;
    font-size: 54px;
    letter-spacing: 4px;
    line-height: 1;
  }
  .brand__tag {
    font-family: "Amatic SC", sans-serif;
    font-weight: 700;
    font-size: 28px;
    letter-spacing: 4px;
    line-height: 1;
  }
  .card--back {
    left: 550px;
    top: 530px;
    text-align: center;
  }
  .contact__name {
    position: absolute;
    top: 62px;
    left: 0;
    right: 0;
    font-family: "Amatic SC", sans-serif;
    font-weight: 400;
    font-size: 52px;
    letter-spacing: 5px;
    line-height: 1;
  }
  .contact__role {
    position: absolute;
    top: 130px;
    left: 0;
    right: 0;
    font-family: "Amatic SC", sans-serif;
    font-weight: 700;
    font-size: 20px;
    letter-spacing: 3px;
    line-height: 1;
  }
  .contact__details {
    position: absolute;
    top: 196px;
    left: 0;
    right: 0;
    list-style: none;
    font-family: "Montserrat", sans-serif;
    font-weight: 500;
    font-size: 15px;
    letter-spacing: 1.5px;
    line-height: 24px;
  }
</style>
</head>
<body>
  <main class="canvas">
    <section class="card card--front" aria-label="Card front">
      <div class="brand">
        <span class="brand__dot" aria-hidden="true"></span>
        <span class="brand__name">Desna Pilou</span>
      </div>
      <p class="brand__tag">Jewellery</p>
    </section>

    <section class="card card--back" aria-label="Card back">
      <h1 class="contact__name">Desna Pilou</h1>
      <p class="contact__role">Designer . Jeweller</p>
      <ul class="contact__details">
        <li>www.desnapilou.com</li>
        <li>info@desnapilou.com</li>
        <li>+61 428 519 203</li>
      </ul>
    </section>
  </main>
</body>
</html>
```